Storefront signage for Physio clinic

We need a design for our storefront windows at our physiotherapy & Pilates clinic.

The design should be modern and include our logo, website url and services (physiotherapy, pilates, massage).

Some inspirational exercise/pilates/recovery quotes may be included and I would like to see the use of sport/pilates/injury related stock images. I have attached a few examples of what we want (images numbered 1-5). And I have attached our current design and photo of the outside of our clinic.

In the attached images there is also a pdf with measurments of our window panels. We require signage for the areas marked 1-10. As you can see on our current signage, you don't need to have a separate image for each panel, these can flow onto each other.

Industry/Entity Type

Clinic

Colors
85acd3
3377b5
3277b5
e8e8e8
c3c3c3
9d9d9d
848484
7f7f7f

Requirements
Must have
• Stock images related to sports, physiotherapy and pilates
• Ideally these images should be in greyscale and blend in with the rest of the panel which should include colours.
• I would like to see for example a runner, a weightlifter, someone doing pilates, someone with back pain (not necessarily all of these).
Should not have
• I want a creative, modern, up market design, not just a standard recycled template.

```html
<!DOCTYPE html>
<html lang="en">
<head>
<meta charset="utf-8">
<title>Harbourside Physiotherapy &amp; Pilates – Storefront Signage</title>
<link rel="stylesheet" href="https://fonts.googleapis.com/css2?family=Questrial&family=Tinos:wght@400;700&family=Montserrat:wght@600&display=swap">
<style>
  :root {
    --bg-top: #f6f6f6;
    --bg-bottom: #d4d4d4;
    --horizon: #bdbdbd;
    --fascia-top: #3a2e28;
    --fascia-bottom: #2a211d;
    --brick-light: #7a6459;
    --brick-dark: #4e3f38;
    --brick-joint: rgba(30, 22, 18, .55);
    --blank: #f4f4f4;
    --blue-deep: #0a3a8c;
    --blue-mid: #1d5fc0;
    --blue-light: #85acd3;
    --door-edge: #c3c3c3;
    --sill: #1e1e1e;
    --label: #222;
    --white: #ffffff;
  }
  * { box-sizing: border-box; margin: 0; padding: 0; }
  html, body { width: 1200px; height: 470px; overflow: hidden; }
  body {
    position: relative;
    background: linear-gradient(var(--bg-top), #e6e6e6 50%, var(--bg-bottom));
    font-family: "Questrial", sans-serif;
  }

  /* Building shell */
  .horizon {
    position: absolute; left: 0; top: 238px; width: 1200px; height: 86px;
    background: linear-gradient(var(--horizon), #cfcfcf);
  }
  .fascia {
    position: absolute; left: 23px; top: 63px; width: 1151px; height: 17px;
    background: linear-gradient(var(--fascia-top), var(--fascia-bottom));
  }
  .pillar {
    position: absolute; top: 80px; height: 244px;
    background:
      repeating-linear-gradient(180deg, transparent 0 18px, var(--brick-joint) 18px 20px),
      repeating-linear-gradient(90deg, transparent 0 13px, var(--brick-joint) 13px 14px),
      linear-gradient(90deg, var(--brick-dark), var(--brick-light) 50%, var(--brick-dark));
  }
  .pillar-outer-left  { left: 23px;   width: 69px; }
  .pillar-left        { left: 378px;  width: 44px; }
  .pillar-right       { left: 696px;  width: 46px; }
  .pillar-outer-right { left: 1106px; width: 68px; }

  /* Windows */
  .window {
    position: absolute;
    top: 80px;
    height: 244px;
    background: var(--blank);
    border-bottom: 6px solid var(--sill);
  }
  .window-header { height: 32px; background: linear-gradient(var(--white), #ececec); }
  .window-left   { left: 92px;  width: 286px; }
  .window-center { left: 422px; width: 274px; }
  .window-right  { left: 742px; width: 364px; }
  .graphic { display: block; width: 100%; height: 206px; }

  .right-row { display: flex; height: 206px; }
  .right-graphic { width: 86px; height: 206px; display: block; }
  .doors {
    width: 192px; height: 238px; margin-top: -32px;
    border: 1px solid var(--door-edge);
    display: flex;
    background: #f7f7f7;
  }
  .door { flex: 1; border: 1px solid #dcdcdc; position: relative; background: linear-gradient(180deg, #fbfbfb, #ececec); }
  .door-handle {
    position: absolute; top: 124px; width: 5px; height: 46px;
    border-radius: 3px; background: linear-gradient(90deg, #aaa, #eee, #999);
  }
  .door:first-child .door-handle { right: 8px; }
  .door:last-child  .door-handle { left: 8px; }

  .info {
    position: relative;
    width: 86px; height: 206px;
    background: linear-gradient(180deg, var(--blue-mid), var(--blue-deep));
    color: var(--white);
    text-align: center;
  }
  .info > * { position: absolute; left: 4px; right: 4px; }
  .brand { top: 14px; display: flex; align-items: center; justify-content: center; gap: 3px; }
  .brand-dot { width: 9px; height: 9px; border-radius: 50%; background: var(--white); flex: none; }
  .brand-name { font-family: "Montserrat", sans-serif; font-weight: 600; font-size: 7.6px; line-height: 1; white-space: nowrap; }
  .brand-tag { top: 26px; font-family: "Montserrat", sans-serif; font-weight: 600; font-size: 4px; padding-left: 10px; white-space: nowrap; }
  .services { top: 77px; list-style: none; }
  .services li {
    font-family: "Tinos", serif; font-size: 5.6px; letter-spacing: .3px; white-space: nowrap;
    padding: 2px 0 3px; border-bottom: .5px solid rgba(255,255,255,.6);
  }
  .services li:last-child { border-bottom: none; }
  .phone { top: 144px; font-family: "Montserrat", sans-serif; font-weight: 600; font-size: 10.5px; white-space: nowrap; }
  .address {
    top: 162px; font-family: "Tinos", serif; font-size: 4.2px; line-height: 1.4;
    border-top: .5px solid rgba(255,255,255,.6); border-bottom: .5px solid rgba(255,255,255,.6);
    padding: 2px 0;
  }
  .url { top: 181px; font-family: "Tinos", serif; font-size: 4px; letter-spacing: .2px; white-space: nowrap; }

  .label {
    position: absolute; top: 352px; font-size: 16px; letter-spacing: 1px; color: var(--label);
    text-align: center;
  }
  .label-left   { left: 92px;  width: 286px; }
  .label-center { left: 422px; width: 274px; }
  .label-right  { left: 742px; width: 364px; }
</style>
</head>
<body>

<div class="horizon"></div>
<div class="fascia"></div>
<div class="pillar pillar-outer-left"></div>
<div class="pillar pillar-left"></div>
<div class="pillar pillar-right"></div>
<div class="pillar pillar-outer-right"></div>

<section class="window window-left">
  <div class="window-header"></div>
  <svg class="graphic" viewBox="0 0 286 206" preserveAspectRatio="none">
    <defs>
      <linearGradient id="bg-blue" x1="0" y1="0" x2="0" y2="1">
        <stop offset="0" stop-color="#2d7fe0"/><stop offset="1" stop-color="#0a3a8c"/>
      </linearGradient>
      <linearGradient id="photo-grey" x1="0" y1="0" x2="1" y2="1">
        <stop offset="0" stop-color="#e8e8e8"/><stop offset=".55" stop-color="#9d9d9d"/><stop offset="1" stop-color="#5a5a5a"/>
      </linearGradient>
    </defs>
    <rect width="286" height="206" fill="url(#bg-blue)"/>
    <path role="img" aria-label="Greyscale photo of a woman stretching over an exercise ball"
          d="M0,78 C40,40 90,22 140,26 L150,186 C90,186 35,170 0,150 Z"
          fill="url(#photo-grey)" stroke="#85acd3" stroke-width="3"/>
    <path role="img" aria-label="Greyscale photo of a group Pilates class doing seated leg exercises"
          d="M190,40 C230,14 270,10 286,12 L286,150 C260,175 230,190 200,194 C210,140 205,80 190,40 Z"
          fill="url(#photo-grey)" stroke="#85acd3" stroke-width="3"/>
    <path role="img" aria-label="Greyscale photo of women in a Pilates class"
          d="M112,20 C185,25 240,110 150,188 C125,140 105,80 112,20 Z"
          fill="url(#photo-grey)" stroke="#3377b5" stroke-width="4"/>
  </svg>
</section>

<section class="window window-center">
  <div class="window-header"></div>
  <svg class="graphic" viewBox="0 0 274 206" preserveAspectRatio="none">
    <defs>
      <linearGradient id="bg-blue-c" x1="0" y1="0" x2="1" y2="1">
        <stop offset="0" stop-color="#0a3a8c"/><stop offset=".5" stop-color="#1d5fc0"/><stop offset="1" stop-color="#2d7fe0"/>
      </linearGradient>
      <linearGradient id="photo-grey-c" x1="0" y1="0" x2="1" y2="1">
        <stop offset="0" stop-color="#f0f0f0"/><stop offset=".6" stop-color="#9d9d9d"/><stop offset="1" stop-color="#4a4a4a"/>
      </linearGradient>
    </defs>
    <rect width="274" height="206" fill="url(#bg-blue-c)"/>
    <path role="img" aria-label="Greyscale photo of a therapist treating a patient lying on a massage table"
          d="M120,55 C170,30 230,30 274,40 L274,180 C230,190 170,200 140,200 C140,150 130,100 120,55 Z"
          fill="url(#photo-grey-c)" stroke="#85acd3" stroke-width="3"/>
    <path role="img" aria-label="Greyscale photo of a runner's legs striding across a grassy hill"
          d="M150,18 C80,30 30,90 28,140 C25,160 15,170 5,172 C40,180 90,190 150,190 C175,130 175,70 150,18 Z"
          fill="url(#photo-grey-c)" stroke="#3377b5" stroke-width="4"/>
  </svg>
</section>

<section class="window window-right">
  <div class="window-header"></div>
  <div class="right-row">
    <svg class="right-graphic" viewBox="0 0 86 206" preserveAspectRatio="none">
      <defs>
        <linearGradient id="bg-blue-r" x1="0" y1="0" x2="0" y2="1">
          <stop offset="0" stop-color="#1d5fc0"/><stop offset="1" stop-color="#0a3a8c"/>
        </linearGradient>
        <radialGradient id="photo-dark-r" cx=".55" cy=".45" r=".7">
          <stop offset="0" stop-color="#9d9d9d"/><stop offset=".6" stop-color="#4a4a4a"/><stop offset="1" stop-color="#1a1a1a"/>
        </radialGradient>
      </defs>
      <rect width="86" height="206" fill="url(#bg-blue-r)"/>
      <path role="img" aria-label="Greyscale photo of a woman lifting dumbbells"
            d="M0,40 C30,20 86,22 86,22 L86,160 C60,175 25,172 0,160 Z"
            fill="url(#photo-dark-r)" stroke="#3377b5" stroke-width="3"/>
    </svg>
    <div class="doors">
      <div class="door"><span class="door-handle"></span></div>
      <div class="door"><span class="door-handle"></span></div>
    </div>
    <aside class="info">
      <div class="brand">
        <span class="brand-dot"></span>
        <span class="brand-name">HARBOURSIDE</span>
      </div>
      <p class="brand-tag">Physiotherapy &amp; Pilates</p>
      <ul class="services">
        <li>PHYSIOTHERAPY</li>
        <li>PILATES</li>
        <li>MASSAGE</li>
        <li>WORK REHABILITATION</li>
      </ul>
      <p class="phone">02 9000 1234</p>
      <p class="address">Shop 12, 40 River St<br>Harbourside NSW 2000</p>
      <p class="url">www.harboursidephysio.com.au</p>
    </aside>
  </div>
</section>

<p class="label label-left">LEFT PANEL</p>
<p class="label label-center">CENTER PANEL</p>
<p class="label label-right">RIGHT PANEL/DOORS</p>

</body>
</html>
```